vantoreq realty business card

We need a Business card for our new business. The logo was designed by BrushQuill, and the text We want on the back is:
REAL ESTATE INVESTMENTS
- BUY, RENOVATE, SELL AND RENT RESIDENTIAL PROPERTIES
- FULL HOME REHABBING , REMODELING AND INTERIOR DESIGN
- HOME STAGING SERVICES
- WHOLESALE INVESTOR PROPERTIES
- MAKE CASH OFFERS ON HOUSES IN ANY CONDITION AND IN ANY SITUATION
- PRIVATE MONEY INVESTOR PROGRAMS WITH 6-12% RETURNS
- PAY CASH REWARDS FOR REFFERALS
- CONCIERGE SERVICE

Business

```html
<!DOCTYPE html>
<html lang="en">
<head>
<meta charset="utf-8">
<title>vantoreq Realty – Business Card</title>
<link rel="stylesheet" href="https://fonts.googleapis.com/css2?family=Open+Sans:wght@400;600&family=Arimo:wght@400&display=swap">
<style>
  :root {
    --backdrop: #a9a7a8;
    --paper: #ffffff;
    --steel-light: #8a8a8c;
    --steel-dark: #5f5f62;
    --steel-deep: #4e4e51;
    --accent: #4fc3d9;
    --silver: #c9cacc;
    --ink-grey: #5c5c5e;
    --text-light: #f4f4f4;
  }
  * { box-sizing: border-box; margin: 0; padding: 0; }
  html, body { width: 1200px; height: 900px; overflow: hidden; }
  body {
    background: var(--backdrop);
    font-family: "Open Sans", sans-serif;
    position: relative;
  }
  .card {
    position: absolute;
    top: 290px;
    width: 540px;
    height: 310px;
    border-radius: 18px;
    overflow: hidden;
  }
  .card--front { left: 40px; background: var(--paper); }
  .card--back { left: 620px; }

  /* front */
  .brand {
    position: absolute;
    top: 0; left: 0; right: 0;
    height: 150px;
    display: flex;
    flex-direction: column;
    align-items: center;
    justify-content: center;
    gap: 6px;
    padding-top: 18px;
  }
  .brand__mark {
    width: 34px; height: 34px;
    background: var(--ink-grey);
    margin-bottom: 12px;
  }
  .brand__name {
    font-size: 26px;
    font-weight: 400;
    color: var(--ink-grey);
    letter-spacing: 0.5px;
    line-height: 1;
  }
  .brand__tagline {
    font-size: 12px;
    color: var(--ink-grey);
    letter-spacing: 1.5px;
  }
  .stripe-accent {
    position: absolute; left: 0; right: 0; top: 156px; height: 8px;
    background: var(--accent);
  }
  .stripe-silver {
    position: absolute; left: 0; right: 0; top: 164px; height: 4px;
    background: var(--silver);
  }
  .steel-surface {
    position: absolute; left: 0; right: 0; top: 168px; bottom: 0;
    background: linear-gradient(180deg, var(--steel-light), var(--steel-dark));
  }
  .card--back .steel-surface {
    top: 0;
    background: linear-gradient(180deg, var(--steel-dark), var(--steel-deep));
  }
  .person {
    position: absolute; top: 200px; left: 0; width: 235px;
    text-align: right; padding-right: 24px;
  }
  .person__name { font-size: 18px; font-weight: 600; color: var(--accent); line-height: 1.2; }
  .person__role { font-size: 10px; color: var(--text-light); }
  .divider {
    position: absolute; left: 246px; top: 186px; width: 1px; height: 100px;
    background: var(--silver);
  }
  .contact {
    position: absolute; left: 262px; top: 186px;
    list-style: none;
    color: var(--text-light);
    font-size: 13px; line-height: 16px;
  }
  .contact li { display: flex; align-items: center; gap: 5px; }
  .contact li.contact__cont { padding-left: 17px; }
  .contact svg { width: 12px; height: 12px; flex: none; }

  /* back */
  .services {
    position: absolute; left: 20px; right: 20px; top: 44px;
    text-align: center;
    font-family: "Arimo", sans-serif;
    text-transform: uppercase;
    list-style: none;
  }
  .services__title {
    color: var(--accent); font-size: 14px; letter-spacing: 0.5px; margin-bottom: 8px;
  }
  .services li { color: var(--text-light); font-size: 11.5px; line-height: 23px; letter-spacing: 0.3px; }
  .back-mark {
    position: absolute; right: 34px; bottom: 56px;
    width: 26px; height: 26px; background: var(--paper);
  }
</style>
</head>
<body>
  <section class="card card--front" aria-label="Business card front">
    <div class="brand">
      <div class="brand__mark" aria-hidden="true"></div>
      <div class="brand__name">VANTOREQRealty</div>
      <div class="brand__tagline">REAL ESTATE SOLUTIONS</div>
    </div>
    <div class="stripe-accent"></div>
    <div class="stripe-silver"></div>
    <div class="steel-surface" role="img" aria-label="Brushed steel perforated texture"></div>
    <div class="person">
      <div class="person__name">Martin Okafor</div>
      <div class="person__role">Executive Director</div>
    </div>
    <div class="divider"></div>
    <ul class="contact">
      <li><svg viewBox="0 0 12 12"><rect x="3" y="0.5" width="6" height="11" rx="1" fill="none" stroke="var(--accent)" stroke-width="1.3"/></svg>555-204-3187</li>
      <li><svg viewBox="0 0 12 12"><path d="M2 1l2.5 0 1 3-1.5 1a6 6 0 0 0 3 3l1-1.5 3 1V11A9 9 0 0 1 1 2z" fill="var(--accent)"/></svg>555-204-6610</li>
      <li><svg viewBox="0 0 12 12"><rect x="1" y="4" width="10" height="7" rx="1" fill="var(--accent)"/><rect x="3" y="1" width="6" height="4" fill="none" stroke="var(--accent)"/></svg>555-204-9052</li>
      <li><svg viewBox="0 0 12 12"><rect x="0.8" y="2.5" width="10.4" height="7" fill="none" stroke="var(--accent)" stroke-width="1.2"/><path d="M1 3l5 4 5-4" fill="none" stroke="var(--accent)" stroke-width="1.2"/></svg>martin@vantoreqrealty.com</li>
      <li><svg viewBox="0 0 12 12"><circle cx="6" cy="6" r="5" fill="none" stroke="var(--accent)" stroke-width="1.2"/><path d="M1 6h10M6 1c-3 3-3 7 0 10M6 1c3 3 3 7 0 10" fill="none" stroke="var(--accent)"/></svg>www.vantoreqrealty.com</li>
      <li><svg viewBox="0 0 12 12"><path d="M6 1L0.5 6H2v5h3V8h2v3h3V6h1.5z" fill="var(--accent)"/></svg>418 W. Elm Street</li>
      <li class="contact__cont">PO Box 318 Halden, NC 27001</li>
    </ul>
  </section>

  <section class="card card--back" aria-label="Business card back">
    <div class="steel-surface" role="img" aria-label="Brushed steel perforated texture"></div>
    <ul class="services">
      <li class="services__title">Real Estate Investments</li>
      <li>Buy, renovate, sell and rent residential properties</li>
      <li>Full home rehabbing , remodeling and interior design</li>
      <li>Home staging services</li>
      <li>Wholesale investor properties</li>
      <li>Make cash offers on houses in any condition and in any situation</li>
      <li>Private money investor programs with 6-12% returns</li>
      <li>Pay cash rewards for refferals</li>
      <li>Concierge service</li>
    </ul>
    <div class="back-mark" aria-hidden="true"></div>
  </section>
</body>
</html>
```